giftware advert design for an tirbo pharmacy which sells giftware, jewellery & handbags

we need a FULL page advert designed for a giftware sale which will be advertised in our local paper and on our zolvique page. So i will need a print ready copy once approved.
the design should have a clear message and have impact.
Our message is to get across the 50% off sale and that the consumer can win a gift voucher. The attached logo should be placed at the bottom of the design. please refer to our previous advert ( see attached) for the standard layout we like to stick to.

Target Market(s)

20-70 age group
women mainly

Industry/Entity Type

Pharmacy

Font styles to use
Serif

Requirements
Must have
• Heading
• KEY INFO:
• A massive 50% off all giftware, handbags & jewellery
• $50 gift voucher to be won every week!!
• Spend $100 or more on giftware to go in the draw
• PROMOTION DATES: Sale ends Sunday 2nd October
• DISCLAIMER: excludes prescriptions & items already on sale. sorry no rain checks or laybys.
Nice to have
• * the key information stand out
• * the store details, address logo etc must be at the bottom of the advert ( please see attached file)
• * disclaimer must be in fine print
Should not have
• * our logo at the top of the design
• * we do not want to look like our competitors (orvanda chemist/ mellowby etc)
• * angry colours

```html
<!DOCTYPE html>
<html lang="en">
<head>
<meta charset="utf-8">
<title>tirbo Giftware Sale</title>
<link rel="stylesheet" href="https://fonts.googleapis.com/css2?family=Roboto+Condensed:wght@300;400;700&family=Arimo:wght@400;700&display=swap">
<style>
  :root {
    --sky: #1ba6df;
    --teal-ink: #0d4b5f;
    --tag-red: #c4262e;
    --orange: #f15a29;
    --orange-light: #f7a23a;
    --brand-blue: #0b72b9;
    --white: #ffffff;
  }
  * { margin: 0; padding: 0; box-sizing: border-box; }
  html, body { width: 848px; height: 1200px; overflow: hidden; background: var(--white); }
  .advert { position: relative; width: 848px; height: 1200px; background: var(--white); overflow: hidden; }
  .artwork { position: absolute; left: 0; top: 0; width: 848px; height: 1200px; }
  .condensed { font-family: "Roboto Condensed", "Arial Narrow", sans-serif; }
  .bold { font-weight: 700; }
  .headline-text { fill: var(--white); }
  .draw-text { fill: var(--tag-red); }
  .sale-ends-text { fill: var(--white); font-weight: 400; }
  .fine-print-text { fill: var(--brand-blue); font-weight: 400; }
  .store-mark { position: absolute; left: 68px; top: 994px; width: 216px; text-align: center; font-family: "Arimo", Arial, sans-serif; color: var(--brand-blue); }
  .store-mark .name { display: flex; align-items: center; justify-content: center; gap: 10px; font-weight: 700; font-size: 44px; line-height: 48px; }
  .store-mark .name i { display: block; width: 30px; height: 30px; background: var(--brand-blue); }
  .store-mark .tagline { font-size: 12.5px; line-height: 16px; }
  .store-mark .centre { margin-top: 10px; font-size: 19px; line-height: 20px; }
  .store-mark .centre b { font-weight: 700; }
  .store-details { position: absolute; left: 312px; top: 1006px; width: 472px; font-family: "Arimo", Arial, sans-serif; color: var(--brand-blue); text-align: right; }
  .store-details .open-line { display: flex; justify-content: space-between; align-items: baseline; }
  .store-details .open { font-weight: 700; font-size: 38px; letter-spacing: -1.5px; line-height: 44px; }
  .store-details .phone { font-family: "Roboto Condensed", sans-serif; font-weight: 300; font-size: 42px; line-height: 44px; letter-spacing: 1px; }
  .store-details .address { margin-top: 4px; font-size: 15.5px; font-weight: 700; line-height: 20px; }
  .store-details .hours { margin-top: 4px; font-size: 10.5px; line-height: 14px; }
</style>
</head>
<body>
<main class="advert">
  <svg class="artwork" viewBox="0 0 848 1200" xmlns="http://www.w3.org/2000/svg">
    <defs>
      <linearGradient id="ribbonFill" x1="0" y1="0" x2="0" y2="1">
        <stop offset="0" stop-color="#f7a23a"/>
        <stop offset="0.12" stop-color="#f15a29"/>
        <stop offset="1" stop-color="#ee5324"/>
      </linearGradient>
      <linearGradient id="foldFill" x1="0" y1="0" x2="1" y2="1">
        <stop offset="0" stop-color="#f47a2c"/>
        <stop offset="1" stop-color="#8a2d17"/>
      </linearGradient>
      <linearGradient id="tagFill" x1="0" y1="0" x2="1" y2="1">
        <stop offset="0" stop-color="#d52c31"/>
        <stop offset="1" stop-color="#ad1f25"/>
      </linearGradient>
      <linearGradient id="inkFill" x1="0" y1="0" x2="0" y2="1">
        <stop offset="0" stop-color="#0f6f86"/>
        <stop offset="1" stop-color="#0d4b5f"/>
      </linearGradient>
    </defs>

    <rect class="sale-band" x="0" y="62" width="848" height="874" fill="#1ba6df"/>

    <g class="discount-ribbon">
      <path d="M320 6 L358 6 Q390 10 390 62 L320 62 Z" fill="url(#foldFill)"/>
      <path d="M24 40 Q24 6 58 6 L322 6 Q342 6 342 30 L342 62 L320 62 L320 340 L170 420 L24 340 Z" fill="url(#ribbonFill)"/>
      <path d="M24 340 L170 420 L320 340" fill="none" stroke="#c9421c" stroke-width="3"/>
      <text class="condensed bold" x="172" y="208" text-anchor="middle" font-size="166" textLength="252" lengthAdjust="spacingAndGlyphs" fill="url(#inkFill)">50%</text>
      <text class="condensed bold" x="172" y="316" text-anchor="middle" font-size="112" textLength="190" lengthAdjust="spacingAndGlyphs" fill="url(#inkFill)">OFF</text>
    </g>

    <g class="headline-text condensed bold" font-size="106">
      <text x="344" y="160" textLength="492" lengthAdjust="spacingAndGlyphs">ALL GIFTWARE,</text>
      <text x="344" y="254" textLength="364" lengthAdjust="spacingAndGlyphs">HANDBAGS</text>
      <text x="344" y="350" textLength="448" lengthAdjust="spacingAndGlyphs">&amp; JEWELLERY</text>
    </g>

    <g class="voucher-tag">
      <path d="M608 356 L792 456 L848 780 L848 800 L572 860 Q556 862 552 846 L476 534 Z"
            fill="url(#tagFill)" stroke="url(#tagFill)" stroke-width="14" stroke-linejoin="round"/>
      <circle cx="611" cy="400" r="24" fill="#1ba6df"/>
      <g transform="translate(522 668) rotate(-15)" fill="#ffffff" class="condensed bold">
        <text x="0" y="0" font-size="215" textLength="262" lengthAdjust="spacingAndGlyphs">$50</text>
        <text x="21" y="60" font-size="42" textLength="270" lengthAdjust="spacingAndGlyphs">GIFT VOUCHER</text>
        <text x="47" y="104" font-size="42" textLength="211" lengthAdjust="spacingAndGlyphs">TO BE WON</text>
        <text x="17" y="146" font-size="42" textLength="258" lengthAdjust="spacingAndGlyphs">EVERY WEEK!!</text>
      </g>
    </g>

    <g class="draw-text condensed bold">
      <text x="54" y="586" font-size="84" textLength="384" lengthAdjust="spacingAndGlyphs">SPEND $100</text>
      <text x="40" y="650" font-size="48" textLength="416" lengthAdjust="spacingAndGlyphs">OR MORE ON GIFTWARE</text>
      <text x="76" y="690" font-size="48" textLength="346" lengthAdjust="spacingAndGlyphs">TO GO IN THE DRAW</text>
    </g>

    <text class="sale-ends-text condensed" x="70" y="916" font-size="58" textLength="708" lengthAdjust="spacingAndGlyphs">SALE ENDS SUNDAY 2<tspan font-size="30" dy="-24">nd</tspan><tspan dy="24"> OCTOBER</tspan></text>

    <text class="fine-print-text condensed" x="38" y="1160" font-size="31" textLength="772" lengthAdjust="spacingAndGlyphs">Excludes prescriptions &amp; items already on sale. Sorry no rain checks or laybys.</text>
  </svg>

  <div class="store-mark">
    <div class="name"><i></i>tirbo</div>
    <div class="tagline">Friendly advice for every family</div>
    <div class="centre"><b>BELMARA</b> VILLAGE</div>
  </div>

  <div class="store-details">
    <div class="open-line"><span class="open">OPEN 7 DAYS</span><span class="phone">4900 5127</span></div>
    <p class="address">Shop 15, Belmara Village, 27 Corran Road, Belmara</p>
    <p class="hours">Mon-Fri 8.30am to 6.30pm &nbsp;|&nbsp; Thurs 8.30am to 7.30pm &nbsp;|&nbsp; Sat and Sun 9.00am to 5.00pm</p>
  </div>
</main>
</body>
</html>
```